Web Design Project: Facility Management company

Hi! We need a new website.

Our current website: http://www.brantel-group.ru/ and we don-t like it. =)
The structure of our company has changed and now we don't need "cleaning" and "engeneering" on this site.

We are facility management company in Russia. So we provide integrated service solutions specific to industrial services: maintenance, repair, etc. of engineering systems.
More services:
Energy planning
Automation
Audit
Statements with regulators
Video surveillance
Central heating
Security systems
Welding
Management of subcontractors
Electrical installation and service needs
Reception
Catering

Visitors:
* Managers in the field of commercial real estate
* Chief engineers
* TOP managers of large companies, malls, factories...
+ their subordinates
* Small% of applicants.

Here you can see some websites/patterns we liked:
http://www.kvelmort.ru/ (This is our competitor’s site, so our site shouldn’t be an exact copy))))
http://www.orbitask.ru/
http://www.layoutpinery.com/demo/24296.html
http://www.layoutpinery.com/website-templates/10145.html

Style:
Light, hi-tech/minimalizm, the color palette should be based on the original site colors (Green + black + white). http://www.brantel-group.ru/

Estimated sitemap:
1. Home
2. About Us
3. Company's policy
4. History + Achievements.
5. Certificates
6. Map of presence (Here you can use sample map in file "our projects")
7. Services
8. Portfolio
9. News or blog
10. Jobs
11. Contacts - with the feedback form (or the function "call to order")
12. English

Need a design pages: main page, page 404. The rest of the page could be created by general pattern.

Logo, navigation bar and contacts should be visible on all pages of a site.
Flash animation elements and buttons, etc. - not needed.

* We need to develop 3 websites, so we are looking for a long term cooperation.
Looking forward to your creativity =)

Must Have:
Clear, intuitive structure of web pages.
In the center - of pictures reflecting our main services (industrial theme). May be in rotation.
BUT! This banner (central picture) should not be a huge one =)
All relevant information should be visible at once without scrolling.

A possibility to place media files (presentations, video ...) and 2 banner links on the main page.

Font should be available in Cyrillic.
Updates

IMPORTANT!

Please notice that in thisdesign we don't need "cleaning" and "engeneering" on this site.

So don't use old block of 4pictures from our current website. We don't need it anymore. 

Thestructure of our company has changed and now we need some links (may be banners,may be something else) to our future cleaning website as well as engeneeringwebsite.
It should look like seperate (partner) companies, not like our sevices.

Regards, Vera.

Please don't forget that we need bilingual site.

So define language changing tool in your designs.

Industry/Entity Type

Industrial

```html
<!DOCTYPE html>
<html lang="en">
<head>
<meta charset="utf-8">
<title>Brantel — Facility Management</title>
<link rel="stylesheet" href="https://fonts.googleapis.com/css2?family=PT+Sans:wght@400;700&display=swap">
<style>
  :root {
    --green: #86a23a;
    --green-dark: #6f8a2a;
    --green-light: #9cb94b;
    --green-text: #8aa437;
    --strip: #4d5e1e;
    --nav-top: #fbfbfb;
    --nav-bottom: #ececec;
    --ink: #4a4a4a;
    --ink-soft: #6a6a6a;
    --panel: rgba(88, 104, 124, 0.92);
    --grey-bg: #efefef;
    --footer: #4b4b4b;
    --white: #ffffff;
  }
  * { box-sizing: border-box; margin: 0; padding: 0; }
  html, body { width: 1200px; height: 737px; overflow: hidden; }
  body {
    position: relative;
    font-family: "PT Sans", Arial, sans-serif;
    color: var(--ink);
    background: var(--white);
  }
  a { text-decoration: none; color: inherit; }

  /* Header */
  .top-strip { position: absolute; left: 0; top: 0; width: 1200px; height: 4px; background: var(--strip); }
  .header {
    position: absolute; left: 0; top: 4px; width: 1200px; height: 48px;
    background: linear-gradient(var(--green-light), var(--green));
  }
  .brand {
    position: absolute; left: 177px; top: 9px;
    display: flex; align-items: center; gap: 6px; color: var(--white);
  }
  .brand-mark { width: 14px; height: 14px; background: var(--white); }
  .brand-name { font-size: 21px; font-weight: 700; letter-spacing: 0.5px; line-height: 1; }
  .brand-sub { position: absolute; left: 20px; top: 23px; font-size: 8.5px; color: var(--white); white-space: nowrap; }
  .phone {
    position: absolute; right: 176px; top: 17px;
    color: var(--white); font-weight: 700; font-size: 13.5px; letter-spacing: 1px;
  }

  /* Navigation */
  .nav {
    position: absolute; left: 0; top: 52px; width: 1200px; height: 72px;
    background: linear-gradient(var(--nav-top), var(--nav-bottom));
    border-top: 1px solid #dcdcdc;
  }
  .nav a {
    position: absolute; top: 30px; font-size: 14px; letter-spacing: 0.8px; color: var(--ink); line-height: 1;
  }
  .nav a.is-active { color: var(--green-text); }

  /* Hero */
  .hero-band {
    position: absolute; left: 0; top: 124px; width: 1200px; height: 238px;
    background: linear-gradient(var(--green-dark), var(--green) 60%, var(--green-light));
  }
  .hero-photo {
    position: absolute; left: 173px; top: 124px; width: 574px; height: 238px;
    background: linear-gradient(160deg, #8fb8e4 0%, #c9dcef 45%, #a9b3a4 70%, #5a6b78 100%);
  }
  .hero-panel {
    position: absolute; left: 747px; top: 124px; width: 281px; height: 238px;
    background: var(--panel); color: var(--white);
    box-shadow: 2px 0 6px rgba(0,0,0,0.2);
  }
  .hero-title {
    position: absolute; left: 18px; top: 11px; width: 260px;
    font-size: 31px; font-weight: 700; line-height: 31px; letter-spacing: 1.2px; text-transform: uppercase;
  }
  .hero-rule { position: absolute; left: 12px; top: 144px; width: 258px; border-top: 1px dotted rgba(255,255,255,0.7); }
  .hero-text { position: absolute; left: 21px; top: 152px; width: 250px; font-size: 11.5px; line-height: 18.5px; }
  .slider-dots {
    position: absolute; left: 537px; top: 339px; width: 90px; height: 27px;
    background: var(--white); border-radius: 3px 3px 0 0;
    display: flex; justify-content: center; align-items: center; gap: 4px;
  }
  .slider-dots span {
    width: 13px; height: 13px; border-radius: 50%;
    background: linear-gradient(#eee, #cfcfcf); border: 1px solid #d0d0d0;
  }
  .slider-dots span.is-current { background: radial-gradient(circle, #777 2px, #e4e4e4 3px); }

  /* Welcome */
  .welcome { position: absolute; left: 0; top: 366px; width: 1200px; height: 109px; background: var(--white); border-bottom: 1px solid #dedede; }
  .welcome-title { position: absolute; left: 176px; top: 12px; font-size: 18.5px; font-weight: 400; letter-spacing: 1px; color: var(--green-text); }
  .welcome-text { position: absolute; left: 177px; top: 42px; width: 560px; font-size: 10.5px; line-height: 18.5px; letter-spacing: 0.3px; color: var(--ink-soft); }
  .read-more { color: var(--green-text); margin-left: 6px; white-space: nowrap; }
  .read-more::after {
    content: ""; display: inline-block; margin-left: 5px;
    border-left: 4px solid var(--green-text); border-top: 3.5px solid transparent; border-bottom: 3.5px solid transparent;
  }
  .cta {
    position: absolute; left: 779px; top: 33px; width: 219px; height: 46px;
    background: linear-gradient(#b4cb62, #8ca83c); border: 1px solid #7d9532; border-radius: 3px;
    color: var(--white); font-weight: 700; font-size: 14.5px; letter-spacing: 0.3px;
    display: flex; align-items: center; justify-content: center;
    text-shadow: 0 1px 1px rgba(0,0,0,0.35);
  }

  /* Features */
  .features { position: absolute; left: 0; top: 475px; width: 1200px; height: 219px; background: var(--grey-bg); }
  .feature { position: absolute; top: 0; width: 257px; }
  .feature-title { position: absolute; left: 6px; top: 21px; font-size: 14px; font-weight: 400; letter-spacing: 0.8px; color: var(--ink); white-space: nowrap; }
  .feature-frame {
    position: absolute; left: 0; top: 47px; width: 257px; height: 94px;
    background: var(--white); box-shadow: 0 0 2px rgba(0,0,0,0.2); padding: 7px;
  }
  .feature-media { width: 100%; height: 100%; background: linear-gradient(120deg, #3e5a74, #7f95a8 50%, #c8a15a 80%, #c9e3a8); }
  .feature-frame.is-video { padding: 0; }
  .feature-frame.is-video .feature-media { background: linear-gradient(90deg, #c9c9c9, #6f7e96 45%, #2f4c84 70%, #3a3a3a); }
  .play { position: absolute; left: 100px; top: 20px; width: 58px; height: 58px; }
  .feature-text { position: absolute; left: 0; top: 154px; width: 257px; font-size: 10.5px; line-height: 19px; letter-spacing: 0.3px; color: var(--ink-soft); }

  /* Footer */
  .footer { position: absolute; left: 0; top: 698px; width: 1200px; height: 39px; background: var(--footer); border-top: 3px solid #e8e8e8; }
  .footer a, .copyright { position: absolute; top: 13px; font-size: 8.5px; color: var(--white); }
  .footer a.is-active { color: var(--green-light); }
  .copyright { right: 174px; }
</style>
</head>
<body>
  <div class="top-strip"></div>
  <header class="header">
    <div class="brand">
      <span class="brand-mark"></span>
      <span class="brand-name">BRANTEL</span>
    </div>
    <span class="brand-sub" style="left:197px;top:31px;position:absolute;">engineering systems</span>
    <span class="phone">+7 812 555 0142</span>
  </header>

  <nav class="nav">
    <a class="is-active" href="#" style="left:173px">Home</a>
    <a href="#" style="left:245px">About Us</a>
    <a href="#" style="left:341px">Policy</a>
    <a href="#" style="left:412px">History</a>
    <a href="#" style="left:486px">Certificates</a>
    <a href="#" style="left:586px">Services</a>
    <a href="#" style="left:671px">Portfolio</a>
    <a href="#" style="left:764px">News</a>
    <a href="#" style="left:834px">Jobs</a>
    <a href="#" style="left:897px">Contact</a>
    <a href="#" style="left:977px">English</a>
  </nav>

  <section class="hero">
    <div class="hero-band"></div>
    <div class="hero-photo" role="img" aria-label="Engineer in hard hat and safety vest with a clipboard in front of an industrial plant"></div>
    <div class="hero-panel">
      <h1 class="hero-title">Full service solutions for industrial companies</h1>
      <div class="hero-rule"></div>
      <p class="hero-text">We are facility management company in Russia. So we provide integrated service solu­tions specific to industrial services: mainte­nance, repair, etc. of engineering systems.</p>
    </div>
    <div class="slider-dots"><span></span><span></span><span></span><span class="is-current"></span></div>
  </section>

  <section class="welcome">
    <h2 class="welcome-title">Welcome to Brantel</h2>
    <p class="welcome-text">Lorem ipsum dolor sit amet, consectetur adipiscing elit. Nulla est mauris, blandit vitae pretium eget, sollici­tudin ac purus. Aenean vel lectus sed leo condimentum pharetra. Cras facilisis sodales semper. Suspendisse luctus semper magna at vulputate <a class="read-more" href="#">read more</a></p>
    <a class="cta" href="#">SPEAK TO AN EXPERT</a>
  </section>

  <section class="features">
    <article class="feature" style="left:171px">
      <h3 class="feature-title">Why Choose Us?</h3>
      <div class="feature-frame"><div class="feature-media" role="img" aria-label="Engineer in hard hat inspecting industrial pipework"></div></div>
      <p class="feature-text">Lorem ipsum dolor sit amet, consectetur adipisc­ing elit. Nulla est mauris, blandit <a class="read-more" href="#">read more</a></p>
    </article>
    <article class="feature" style="left:471px">
      <h3 class="feature-title">What we can do?</h3>
      <div class="feature-frame"><div class="feature-media" role="img" aria-label="Engineer in hard hat inspecting industrial pipework"></div></div>
      <p class="feature-text">Lorem ipsum dolor sit amet, consectetur adipisc­ing elit. Nulla est mauris, blandit <a class="read-more" href="#">read more</a></p>
    </article>
    <article class="feature" style="left:770px">
      <h3 class="feature-title">Watch our video</h3>
      <div class="feature-frame is-video">
        <div class="feature-media" role="img" aria-label="Video preview: hand touching a set of blue gears"></div>
        <svg class="play" viewBox="0 0 58 58" aria-hidden="true">
          <circle cx="29" cy="29" r="28" fill="rgba(255,255,255,0.55)"/>
          <path d="M22 17 L42 29 L22 41 Z" fill="#3d3d3d"/>
        </svg>
      </div>
      <p class="feature-text">Lorem ipsum dolor sit amet, consectetur adipisc­ing elit. Nulla est mauris, blandit <a class="read-more" href="#">read more</a></p>
    </article>
  </section>

  <footer class="footer">
    <a class="is-active" href="#" style="left:173px">Home</a>
    <a href="#" style="left:235px">About</a>
    <a href="#" style="left:297px">News</a>
    <a href="#" style="left:357px">Jobs</a>
    <a href="#" style="left:403px">Contact</a>
    <span class="copyright">Copyright 2012</span>
  </footer>
</body>
</html>
```